Letterhead for denture company

We need a letterhead designed for our denture company called "Brightbite" We have attached the logo and business card with the colours on them that we like

Target Market(s)

Everyone aged 45+

Industry/Entity Type

Dental Clinic

Font styles to use
Serif
Sans Serif

Colors
3276b5
f37122

Requirements
Must have
• The colours used in our business card
• Be bold and modern
• Thick fonts
• Logo
Nice to have
• Elements that could tie in nicely with any future signage or website upgrades
Should not have
• Thin font
• Should not be too busy

```html
<!DOCTYPE html>
<html lang="en">
<head>
<meta charset="utf-8">
<title>Brightbite Letterhead</title>
<link rel="stylesheet" href="https://fonts.googleapis.com/css2?family=Exo+2:wght@500;600&family=Libre+Franklin:wght@400&display=swap">
<style>
  :root {
    --brand-blue: #0075b8;
    --brand-orange: #e2682a;
    --paper: #ffffff;
    --page-edge: #8a8a8a;
    --on-blue: #ffffff;
  }
  html, body {
    margin: 0;
    padding: 0;
    width: 849px;
    height: 1200px;
    overflow: hidden;
    background: var(--paper);
  }
  .letterhead {
    position: relative;
    width: 849px;
    height: 1200px;
    background: var(--paper);
    box-sizing: border-box;
    border: 1px solid var(--page-edge);
    overflow: hidden;
  }
  .header-bands {
    position: absolute;
    left: 0;
    top: 0;
    width: 849px;
    height: 220px;
    display: block;
  }
  .band-blue { fill: var(--brand-blue); }
  .band-orange { fill: var(--brand-orange); }
  .brand {
    position: absolute;
    left: 30px;
    top: 33px;
    width: 336px;
    text-align: center;
    color: var(--on-blue);
  }
  .brand-square {
    display: block;
    width: 70px;
    height: 70px;
    margin: 0 auto;
    background: var(--on-blue);
    border-radius: 3px;
  }
  .brand-name {
    margin: 8px 0 0;
    font-family: "Exo 2", sans-serif;
    font-weight: 600;
    font-size: 37px;
    letter-spacing: 1px;
    line-height: 1;
    text-transform: uppercase;
  }
  .brand-tagline {
    margin: 8px 0 0;
    font-family: "Exo 2", sans-serif;
    font-weight: 600;
    font-size: 15px;
    letter-spacing: 3.4px;
    line-height: 1;
    text-transform: uppercase;
  }
  .contact {
    position: absolute;
    left: 587px;
    top: 29px;
    font-family: "Libre Franklin", sans-serif;
    font-weight: 400;
    font-size: 16px;
    line-height: 20px;
    color: var(--on-blue);
  }
  .contact p { margin: 0; }
  .contact-lines { margin-top: 16px !important; }
</style>
</head>
<body>
  <div class="letterhead">
    <svg class="header-bands" viewBox="0 0 849 220" aria-hidden="true">
      <path class="band-blue" d="M0 0 H849 V210 H604 C586 210 575 203 566 192 L556 180 C552 176 548 174 540 174 H0 Z"/>
      <path class="band-orange" d="M0 178 H554 L562 190 H0 Z"/>
    </svg>

    <div class="brand">
      <span class="brand-square"></span>
      <p class="brand-name">Brightbite</p>
      <p class="brand-tagline">The Denture Experts</p>
    </div>

    <div class="contact">
      <p>148 Harbour View Road</p>
      <p>Westmere Park, Auckland 0612</p>
      <p>www.brightbite.co.nz</p>
      <div class="contact-lines">
        <p>P: 0800 55 7000</p>
        <p>C: 094127735</p>
        <p>sam@brightbite.co.nz</p>
      </div>
    </div>
  </div>
</body>
</html>
```